Local electrical company needs two flyers designed

We are a small local electrical contracting company and are in desperate need of a awasome flyer design to help grow our business

hi everyone.

please keep the logo off the front page.
it can go on the rear.

We are really trying to portray a angry/frustrated women BECAUSE her lights are broken.
not light globes

Target Market(s)

Home owners

Industry/Entity Type

Electrical

Font styles to use
Serif

Requirements
Nice to have

```html
<!DOCTYPE html>
<html lang="en">
<head>
<meta charset="utf-8">
<title>Lighting Replacement Flyer</title>
<link rel="stylesheet" href="https://fonts.googleapis.com/css2?family=Fira+Sans:wght@500&family=Montserrat:wght@700;800&display=swap">
<style>
  :root {
    --page-bg: #2a2a2a;
    --flyer-black: #050506;
    --photo-deep: #141116;
    --photo-plum: #4a3650;
    --photo-violet: #5a4466;
    --photo-slate: #5b5f66;
    --photo-stone: #6c6a66;
    --photo-skin: #7a6458;
    --headline-white: #ffffff;
    --offer-yellow: #ffd500;
  }
  * { margin: 0; padding: 0; box-sizing: border-box; }
  html, body {
    width: 1200px;
    height: 900px;
    overflow: hidden;
    background: var(--page-bg);
  }
  .flyer {
    position: absolute;
    left: 50px;
    top: 62px;
    width: 1100px;
    height: 776px;
    background: var(--flyer-black);
    overflow: hidden;
  }
  .hero-photo {
    position: absolute;
    inset: 0;
    background:
      radial-gradient(ellipse 150px 130px at 720px 230px, rgba(122,100,88,0.55) 0%, rgba(122,100,88,0) 100%),
      radial-gradient(ellipse 170px 260px at 800px 520px, rgba(122,100,88,0.45) 0%, rgba(122,100,88,0) 100%),
      radial-gradient(ellipse 240px 340px at 690px 430px, var(--photo-slate) 0%, rgba(91,95,102,0.55) 50%, rgba(91,95,102,0) 100%),
      radial-gradient(ellipse 260px 70px at 800px 735px, rgba(108,106,102,0.7) 0%, rgba(108,106,102,0) 100%),
      radial-gradient(ellipse 300px 260px at 1010px 230px, var(--photo-violet) 0%, rgba(90,68,102,0.4) 55%, rgba(90,68,102,0) 100%),
      radial-gradient(ellipse 260px 160px at 1020px 640px, rgba(74,54,80,0.85) 0%, rgba(74,54,80,0) 100%),
      linear-gradient(90deg, var(--flyer-black) 0%, var(--flyer-black) 36%, var(--photo-deep) 48%, #231c27 70%, #2e2333 100%);
  }
  .copy {
    position: absolute;
    left: 52px;
    color: var(--headline-white);
    font-family: "Fira Sans", sans-serif;
    font-weight: 500;
  }
  .headline {
    top: 64px;
    font-size: 58px;
    line-height: 68px;
    letter-spacing: -0.2px;
  }
  .subhead {
    top: 224px;
    font-size: 30px;
    line-height: 37px;
  }
  .question {
    top: 346px;
    font-size: 58px;
    line-height: 72px;
    letter-spacing: -0.2px;
  }
  .offer-bar {
    position: absolute;
    left: 0;
    top: 559px;
    width: 29px;
    height: 166px;
    background: var(--offer-yellow);
    border-radius: 0 14px 14px 0;
  }
  .offer {
    position: absolute;
    left: 52px;
    color: var(--offer-yellow);
    font-family: "Montserrat", sans-serif;
    white-space: nowrap;
  }
  .offer-amount {
    top: 534px;
    font-size: 134px;
    font-weight: 800;
    line-height: 156px;
    letter-spacing: 3px;
  }
  .offer-detail {
    top: 689px;
    font-size: 35px;
    font-weight: 700;
    line-height: 42px;
    letter-spacing: 1.5px;
  }
</style>
</head>
<body>
  <main class="flyer">
    <div class="hero-photo" role="img" aria-label="Photo of a frustrated woman sitting hunched on a chair in a dim living room, hugging her knees"></div>

    <h1 class="copy headline">Is your lighting<br>frustrating you?</h1>
    <p class="copy subhead">Tired of coming<br>home to lights that<br>don't always work?</p>
    <p class="copy question">Thinking<br>of a change?</p>

    <div class="offer-bar"></div>
    <p class="offer offer-amount">SAVE $25</p>
    <p class="offer offer-detail">OFF YOUR LIGHTING REPLACEMENT</p>
  </main>
</body>
</html>
```